依頼詳細
はがきサイズで、こちらで印刷して渡す予定ですので
サイズははがきサイズにて作成をお願いします。
また、以下の文面を入れて作成をお願いします。

あなたの素晴らしい「チャレンジ」に心から感謝致します。
1年間ありがとうございました。
緑丘カメリアクラブ 第63代会長 森川 透

文字の書体や大きさに関しては指定ありません、お任せします。
また添付ファイル2つも、どこかに入れ込んでいただきたいです。
・クラブのロゴ
・会長の似顔絵
記載項目
1年間ありがとうございました。
緑丘カメリアクラブ 第63代会長 森川 透
希望イメージ
シンプル 複雑
単色 カラフル
暗い 明るい
日常 高級
遊び心 厳粛
未来的 伝統的
女性的 男性的
希望する色
納品ファイル
• 高解像度JPG (.jpg)
補足説明
6月23日に使用する予定の為、あまり時間がありません。
そのため良いなと思うものがありましたら、即決する予定です。

パッと見た瞬間に、イメージの通りと感じたので、こちらに決めさせて頂きました。

この度は多くの提案、誠にありがとうございました。
どれも魅力的で、正直とても迷ってしまい、決定が遅くなってしまいました。
また機会がありましたら、どうぞよろしくお願い致します。

```html
<!DOCTYPE html>
<html lang="ja">
<head>
<meta charset="UTF-8">
<title>感謝カード</title>
<link rel="stylesheet" href="https://fonts.googleapis.com/css2?family=Shippori+Mincho:wght@500;600;700&display=swap">
<style>
  :root {
    --stripe-pink: #f6d4db;
    --stripe-white: #fdf7f8;
    --panel: #ffffff;
    --gold: #b8995a;
    --gold-text: #9c7b3c;
    --ink: #3a3a3a;
    --sub-ink: #5a4e44;
    --rose-light: #f9dbe2;
    --rose-mid: #f0b5c3;
  }
  * { margin: 0; padding: 0; box-sizing: border-box; }
  html, body { width: 847px; height: 1200px; overflow: hidden; }
  body {
    position: relative;
    font-family: "Shippori Mincho", serif;
    background: repeating-linear-gradient(90deg,
      var(--stripe-pink) 0 23px, var(--stripe-white) 23px 46px);
  }
  .panel {
    position: absolute;
    left: 100px; top: 210px;
    width: 647px; height: 855px;
    background: var(--panel);
  }
  .panel-frame { position: absolute; left: 92px; top: 202px; }
  .roses {
    position: absolute;
    left: 240px; top: 28px;
    width: 367px; height: 240px;
    border-radius: 40px;
    background: linear-gradient(135deg, var(--rose-light), var(--rose-mid) 50%, var(--rose-light));
  }
  .message {
    position: absolute;
    left: 100px; width: 647px; top: 332px;
    text-align: center;
  }
  .message-main {
    font-size: 46px; font-weight: 600;
    line-height: 78px; letter-spacing: 1px;
    color: var(--gold-text);
  }
  .message-sub {
    margin-top: 30px;
    font-size: 25px; font-weight: 500;
    color: var(--sub-ink);
  }
  .club-mark {
    position: absolute;
    left: 323px; top: 712px; width: 200px;
    text-align: center;
    font-size: 22px; font-weight: 700;
    color: var(--gold-text);
  }
  .club-mark::before {
    content: "";
    display: block;
    width: 78px; height: 78px;
    margin: 0 auto 8px;
    border-radius: 50%;
    background: var(--gold);
  }
  .signature {
    position: absolute;
    right: 222px; top: 880px;
    text-align: right;
    color: var(--ink);
  }
  .signature-club { font-size: 28px; font-weight: 600; letter-spacing: 1px; }
  .signature-title { font-size: 18px; margin-top: 10px; }
  .signature-title .name { font-size: 28px; font-weight: 600; margin-left: 14px; letter-spacing: 2px; }
  .portrait {
    position: absolute;
    left: 640px; top: 865px;
    width: 88px; height: 108px;
    border-radius: 10px;
    background: linear-gradient(180deg, #efe6de, #dccdc0);
  }
</style>
</head>
<body>
  <div class="panel"></div>
  <svg class="panel-frame" width="663" height="871" viewBox="0 0 663 871" aria-hidden="true">
    <rect x="3" y="3" width="657" height="865" rx="14" fill="none" stroke="var(--gold)" stroke-width="4"/>
    <rect x="14" y="14" width="635" height="843" rx="8" fill="none" stroke="var(--gold)" stroke-width="1.5"/>
  </svg>
  <div class="roses" role="img" aria-label="ピンクのバラ二輪と葉のイラスト"></div>

  <div class="message">
    <p class="message-main">あなたの素晴らしい<br>「チャレンジ」に<br>心から感謝致します。</p>
    <p class="message-sub">1年間ありがとうございました。</p>
  </div>

  <div class="club-mark">緑丘会</div>

  <div class="signature">
    <p class="signature-club">緑丘カメリアクラブ</p>
    <p class="signature-title">第63代会長<span class="name">森川 透</span></p>
  </div>
  <div class="portrait" role="img" aria-label="会長の似顔絵"></div>
</body>
</html>
```